Slick Web Design for Health Care Software Company

We need a new corporate web design for our company, "Brivora." We specialize in web-based cloud software geared toward helping health care professionals.

Our focus for our home site is our products and services. We want potential clients and medical boards who visit our site to have an immediate sense of professionalism and know-how. Our products are innovative, easy to use, and customizable. Users should get this feel when visiting our site.

This is a link to our previous site: www.brivorainc.example. This site is too busy, the colors are too dark, and there's too much information in each page. When creating a design, feel free to eliminate the plethora of info present in the old site.

We have a logo and content for our site that we're going to use. For each of the 7-10 products and services, there is going to be a short 1-2 paragraph excerpt on their own page, as well as a case study related to each. Other parts that can be integrated into the site are our portfolio of clients, newsletter, and about us/contact us.

Some websites to use as general inspiration:
http://www.quellsite.example/
http://www.vantrex.example/
http://www.telmaroplans.example/

Target Market(s)

Health Care Professionals from Specialty Organizations and Boards

Industry/Entity Type

Health Care

Requirements
Nice to have
• Our trademark slogan is "Turn data in knowledge, knowledge into improvement." It would be pretty sweet to integrate this idea into the design of the site.

Also, BE CREATIVE. AVOID TRADITIONAL DESIGNS. Try to exemplify innovation within clarity.
Should not have
• Avoid dark backgrounds.

```html
<!DOCTYPE html>
<html lang="en">
<head>
<meta charset="utf-8">
<title>Brivora – Turn data into knowledge</title>
<link href="https://fonts.googleapis.com/css2?family=Open+Sans:wght@400;600;700&display=swap" rel="stylesheet">
<style>
:root{
  --blue:#2b8fd6;
  --blue-deep:#1c6fb5;
  --blue-light:#dcecf8;
  --blue-pale:#eef6fc;
  --green:#7cb928;
  --orange:#f39a1e;
  --ink:#3b3b3b;
  --muted:#7a7a7a;
  --line:#d6dde3;
  --white:#ffffff;
  --footer:#f3f5f7;
}
*{margin:0;padding:0;box-sizing:border-box}
html,body{width:761px;height:1200px;overflow:hidden;background:var(--white)}
body{font-family:"Open Sans",Arial,sans-serif;color:var(--ink);font-size:9px;line-height:1.4}
.page{position:relative;width:761px;height:1200px}

/* header */
.site-header{height:38px;display:flex;align-items:center;justify-content:space-between;padding:0 26px;background:var(--white)}
.brand{display:flex;align-items:center;gap:6px;font-weight:700;font-size:17px;color:var(--green)}
.brand-dot{width:12px;height:12px;border-radius:50%;background:var(--green)}
.main-nav{display:flex;gap:2px}
.main-nav a{display:block;padding:5px 12px;font-size:9px;color:var(--muted);text-decoration:none}
.main-nav a.active{background:var(--blue);color:var(--white);border-radius:2px}

/* hero */
.hero{position:relative;height:318px;background:linear-gradient(180deg,#4aa8e6 0%,#8fcaf0 60%,#d9eefb 100%);overflow:hidden}
.hero h1{position:absolute;top:18px;left:0;right:0;text-align:center;color:var(--white);font-size:27px;font-weight:600;letter-spacing:-.3px}
.hero p{position:absolute;top:58px;left:0;right:0;text-align:center;color:#eaf5fd;font-size:11px}
.hero-art{position:absolute;left:185px;top:92px;width:510px;height:215px;border-radius:6px;
  background:radial-gradient(ellipse at 30% 50%,#f4fbff 0%,#bfe0f6 45%,rgba(160,205,238,.4) 75%),linear-gradient(90deg,#d6ecfa,#9fcdee)}

/* news */
.news{height:78px;display:flex;align-items:center;justify-content:space-between;padding:0 26px;border-bottom:1px solid var(--line)}
.news-body{width:460px}
.news h2{display:flex;align-items:center;gap:6px;font-size:11px;color:var(--ink);font-weight:700;margin-bottom:4px}
.news-icon{width:14px;height:14px;border-radius:3px;background:var(--blue)}
.news p{font-size:7.5px;color:var(--muted)}
.btn-subscribe{display:inline-block;background:var(--orange);color:var(--white);font-weight:700;font-size:10px;padding:9px 22px;border-radius:4px}

/* products */
.products{height:260px;display:flex;justify-content:space-between;align-items:flex-start;padding:30px 40px 0;border-bottom:1px solid var(--line)}
.product{width:200px;text-align:center}
.product-icon{width:38px;height:32px;margin:0 auto 8px;border-radius:5px;background:linear-gradient(180deg,#5fb0e6,var(--blue-deep))}
.product h3{font-size:11px;font-weight:700;color:var(--ink);margin-bottom:6px}
.product p{font-size:7.5px;color:var(--muted);margin-bottom:12px}
.btn-more{display:inline-block;padding:5px 14px;border:1px solid var(--line);border-radius:3px;font-size:8px;color:var(--muted);background:linear-gradient(#fff,#eef1f3)}

/* services & cases */
.info-band{display:flex;gap:30px;margin-top:12px;padding:18px 26px 0;background:var(--blue-pale);border-top:1px solid var(--blue-light);border-bottom:1px solid var(--blue-light);height:300px}
.col{flex:1}
.col h2{font-size:19px;font-weight:600;color:var(--blue);margin-bottom:2px}
.col .lead{font-size:8px;color:var(--muted);margin-bottom:8px}
.services h3{font-size:11px;color:var(--green);font-weight:700;margin-bottom:4px}
.services ul{list-style:none;font-size:8px;color:var(--muted)}
.services li{padding:1px 0 1px 12px;position:relative}
.services li::before{content:"";position:absolute;left:0;top:5px;width:5px;height:5px;border-radius:50%;background:var(--blue)}
.btn-find{display:inline-block;margin-top:10px;background:var(--green);color:var(--white);font-weight:700;font-size:10px;padding:8px 22px;border-radius:4px}
.case{display:flex;gap:10px;margin-bottom:10px}
.case-thumb{flex:none;width:70px;height:48px;border:1px solid var(--line);background:linear-gradient(135deg,#f7fbfe,#cfe4f4)}
.case a{font-size:8.5px;color:var(--blue);text-decoration:none;display:block}
.case strong{display:block;font-size:8.5px;color:var(--ink)}
.case p{font-size:7.5px;color:var(--muted)}
.cases .btn-find{margin-top:0}

/* footer */
.site-footer{display:flex;gap:40px;padding:18px 26px 0;background:var(--footer);height:160px}
.site-footer h4{font-size:11px;font-weight:700;color:var(--ink);margin-bottom:6px}
.about{width:300px}
.about h5{font-size:10px;color:var(--blue);font-weight:600;margin-bottom:4px}
.about p{font-size:7.5px;color:var(--muted)}
.about a{font-size:7.5px;color:var(--blue)}
.resources{width:130px}
.resources ul{list-style:none;font-size:8px;color:var(--muted)}
.resources li{padding:2px 0 2px 10px;position:relative}
.resources li::before{content:"";position:absolute;left:0;top:7px;width:4px;height:4px;background:var(--blue)}
.touch{flex:1}
.touch label{display:block;font-size:8px;color:var(--muted);margin-bottom:4px}
.field{height:20px;border:1px solid var(--line);background:var(--white);font-size:8px;color:var(--muted);padding:4px 6px;margin-bottom:8px}
.socials{display:flex;gap:5px}
.socials span{width:16px;height:16px;border-radius:3px;background:var(--blue)}

.bottom-bar{position:absolute;left:0;right:0;bottom:0;height:34px;display:flex;align-items:center;justify-content:space-between;padding:0 26px;border-top:3px solid var(--blue);background:var(--white);font-size:7.5px;color:var(--muted)}
.bottom-bar .brand{font-size:13px}
.bottom-bar .brand-dot{width:9px;height:9px}
</style>
</head>
<body>
<div class="page">
  <header class="site-header">
    <div class="brand"><span class="brand-dot"></span>Brivora</div>
    <nav class="main-nav">
      <a class="active" href="#">Home</a><a href="#">About Us</a><a href="#">Services</a><a href="#">Products</a><a href="#">Resources</a><a href="#">Contact us</a>
    </nav>
  </header>

  <section class="hero">
    <h1>Turn data into knowledge, knowledge into improvement</h1>
    <p>Your partner in Clinical Performance Improvement and CME that make a difference for health care providers and patients.</p>
    <div class="hero-art" role="img" aria-label="Illustration of a laptop with a data-to-improvement cycle diagram and a light bulb"></div>
  </section>

  <section class="news">
    <div class="news-body">
      <h2><span class="news-icon"></span>Latest News</h2>
      <p>Brivora releases its 2013 web registry update with new reporting tools for members and partners.<br>
      There is still time to enroll for CME. The deadline for certification is fast approaching, so please review your plan with our support team today.</p>
    </div>
    <span class="btn-subscribe">Subscribe for our newsletter</span>
  </section>

  <section class="products">
    <div class="product">
      <div class="product-icon" role="img" aria-label="Online learning icon"></div>
      <h3>Online Learning / CME</h3>
      <p>Provide targeted online CME and tools to meaningfully measure and educate learners that are seeking to improve their patient care practices.</p>
      <span class="btn-more">Learn More</span>
    </div>
    <div class="product">
      <div class="product-icon" role="img" aria-label="Performance improvement platform icon"></div>
      <h3>Performance Improvement<br>Platform</h3>
      <p>Do you need a place to design, develop and implement a quality improvement or performance program within your health care organization?</p>
      <span class="btn-more">Learn More</span>
    </div>
    <div class="product">
      <div class="product-icon" role="img" aria-label="Registry system icon"></div>
      <h3>PQRS/PRO Registry System</h3>
      <p>The information on this registry is powerful for ensuring health care providers and the government receive quality measure updates as quickly as possible.</p>
      <span class="btn-more">Learn More</span>
    </div>
  </section>

  <section class="info-band">
    <div class="col services">
      <h2>Services</h2>
      <p class="lead">Our areas of development experience and system differences will benefit you!</p>
      <h3>Our areas of expertise include</h3>
      <ul>
        <li>Health care education and outcomes development</li>
        <li>Online CME</li>
        <li>Performance Improvement (PI) CME / Part IV MOC</li>
        <li>Registry reporting PQRS and other PIP initiatives</li>
        <li>Self-Assessment (SAM / Part II MOC)</li>
        <li>Virtual Conferences</li>
        <li>Evaluations and Surveys</li>
        <li>Statistics Analysis and Quality Improvement</li>
        <li>Education Tracking and Assessment</li>
        <li>Learning Management Systems (LMS)</li>
        <li>Content Managed Systems (CMS)</li>
      </ul>
      <span class="btn-find">Find out more</span>
    </div>
    <div class="col cases">
      <h2>Case Studies</h2>
      <div class="case">
        <div class="case-thumb" role="img" aria-label="Screenshot of a fellows portal website"></div>
        <div>
          <a href="#">www.glandwellportal.example</a>
          <strong>The Glandwell Society</strong>
          <p>When Glandwell collaborated with the professionals of 2010 to 2016 to improve a clinical program of their fellows.</p>
        </div>
      </div>
      <div class="case">
        <div class="case-thumb" role="img" aria-label="Screenshot of a practice improvement website"></div>
        <div>
          <a href="#">http://www.practicelab.example/pi/</a>
          <p>This track of professional education and feedback enabled inclusion of the collaborative development of the society to best educate its members, determine measures for effective networking.</p>
        </div>
      </div>
      <div class="case">
        <div class="case-thumb" role="img" aria-label="Screenshot of a kidney fellows website"></div>
        <div>
          <strong>Northfield Renal Council – Kidney Fellows PSM</strong>
          <p>In another ongoing development partnership, the council and Brivora teamed together with members to deliver a Part IV Practice Improvement module.</p>
        </div>
      </div>
      <span class="btn-find">Find out more cases</span>
    </div>
  </section>

  <footer class="site-footer">
    <div class="about">
      <h4>About Us</h4>
      <h5>The Brivora Team</h5>
      <p>Our success is a result of our many talented professionals combining years of knowledge and experience in a broad range of relevant applications. We combine innovative technology and creative service with training focus to ensure high-quality performance improvement and practice change management.</p>
      <a href="#">www.brivorainc.example</a>
    </div>
    <div class="resources">
      <h4>Resources</h4>
      <ul><li>Meeting</li><li>Regulation</li><li>Partners</li><li>Policies</li><li>Brivora Blog</li></ul>
    </div>
    <div class="touch">
      <h4>Stay in touch</h4>
      <label>Signup our Newsletter</label>
      <div class="field">info@brivorainc.example</div>
      <div class="socials"><span></span><span></span><span></span></div>
    </div>
  </footer>

  <div class="bottom-bar">
    <span>Copyright 2013 Brivora. All rights reserved. | Terms of Use | Privacy Policy</span>
    <div class="brand"><span class="brand-dot"></span>Brivora</div>
  </div>
</div>
</body>
</html>
```